Business card for consulting firm

We need a double-sided business card for consulting firm, VantoriX. The card should be professional but also creative and visually interesting.

Target Market(s)

Engineering and technology; transport industries; safety critical / heavy industry.

Contact Information for Business Card

See attached file with details.

Font styles to use
Sans Serif

```html
<!DOCTYPE html>
<html lang="en">
<head>
<meta charset="utf-8">
<title>VantoriX Business Card</title>
<link href="https://fonts.googleapis.com/css2?family=Montserrat:ital,wght@0,400;0,500;0,600;1,400&family=Roboto:wght@400&display=swap" rel="stylesheet">
<style>
  :root {
    --page-bg: #b4b4b4;
    --navy: #0b2236;
    --navy-deep: #062539;
    --teal: #1a7b9d;
    --accent: #1ea0cf;
    --card-white: #f3f3f3;
    --text-dark: #1b1f24;
    --front-text: #e8ecef;
  }
  * { margin: 0; padding: 0; box-sizing: border-box; }
  html, body { width: 1200px; height: 576px; overflow: hidden; }
  body { background: var(--page-bg); position: relative; font-family: "Montserrat", sans-serif; }

  .card {
    position: absolute; top: 138px; height: 294px; border-radius: 13px; overflow: hidden;
    box-shadow: 0 3px 6px rgba(0,0,0,0.25);
  }
  .card-front { left: 82px; width: 484px; }
  .card-back { left: 602px; width: 481px; background: var(--card-white); }

  .front-field {
    position: absolute; inset: 0;
    background: linear-gradient(180deg, var(--navy-deep) 0%, #0e4966 50%, var(--teal) 100%);
  }
  .front-wordmark {
    position: absolute; left: 0; right: 0; top: 127px; text-align: center;
    font-weight: 600; font-size: 44px; line-height: 54px; letter-spacing: 1px; color: var(--front-text);
  }
  .front-url {
    position: absolute; left: 0; right: 0; top: 265px; text-align: center;
    font-size: 12px; line-height: 14px; color: #c8dbe4; letter-spacing: 0.2px;
  }

  .back-decor {
    position: absolute; left: 238px; top: 0; width: 243px; height: 200px;
    background: radial-gradient(ellipse at 70% 30%, rgba(30,160,207,0.16) 0%, rgba(30,160,207,0.06) 55%, rgba(30,160,207,0) 80%);
  }
  .back-wordmark {
    position: absolute; left: 26px; top: 128px;
    font-weight: 600; font-size: 31px; line-height: 38px; letter-spacing: 0.5px; color: var(--navy);
  }

  .holder-name, .holder-credentials, .holder-role { position: absolute; left: 260px; white-space: nowrap; }
  .holder-name { top: 80px; font-size: 18px; line-height: 22px; font-weight: 500; color: var(--text-dark); }
  .holder-credentials { top: 103px; font-family: "Roboto", sans-serif; font-size: 10px; line-height: 12px; color: #333; }
  .holder-role { top: 118px; font-size: 12px; line-height: 15px; font-style: italic; color: var(--accent); }

  .contact-list { position: absolute; left: 262px; top: 145px; list-style: none; }
  .contact-item { display: flex; align-items: center; height: 17px; font-size: 12px; line-height: 17px; color: var(--text-dark); white-space: nowrap; }
  .contact-icon { width: 10px; height: 10px; margin-right: 7px; flex: none; }

  .back-footer { position: absolute; left: 0; bottom: 0; width: 481px; height: 38px; }
  .footer-url {
    position: absolute; left: 260px; top: 265px; font-size: 12px; line-height: 14px; color: #e6eef2; letter-spacing: 0.2px;
  }
</style>
</head>
<body>
  <section class="card card-front">
    <div class="front-field" role="img" aria-label="Deep navy to teal background with a soft organic cell pattern"></div>
    <div class="front-wordmark">VantoriX</div>
    <div class="front-url">www.vantorix.com.au</div>
  </section>

  <section class="card card-back">
    <div class="back-decor" role="img" aria-label="Faint light blue cell pattern decoration"></div>
    <div class="back-wordmark">VantoriX</div>

    <p class="holder-name">Helena Marsh</p>
    <p class="holder-credentials">BA (Hons), M Psych Org, M Tech Mgt (HF)</p>
    <p class="holder-role">Managing Director</p>

    <ul class="contact-list">
      <li class="contact-item">
        <svg class="contact-icon" viewBox="0 0 10 10"><circle cx="5" cy="5" r="4.3" fill="none" stroke="#1ea0cf" stroke-width="1"/><path d="M3.4 3 L4.2 2.8 L4.6 3.9 L4.1 4.3 Q4.6 5.4 5.7 5.9 L6.1 5.4 L7.2 5.8 L7 6.6 Q4 6.8 3.4 3Z" fill="#1ea0cf"/></svg>
        +61 (0)400 555 018
      </li>
      <li class="contact-item">
        <svg class="contact-icon" viewBox="0 0 10 10"><rect x="0.8" y="2" width="8.4" height="6" fill="none" stroke="#1ea0cf" stroke-width="1"/><path d="M0.8 2 L5 5.4 L9.2 2" fill="none" stroke="#1ea0cf" stroke-width="1"/></svg>
        hmarsh@vantorix.com.au
      </li>
      <li class="contact-item">
        <svg class="contact-icon" viewBox="0 0 10 10"><circle cx="5" cy="5" r="4.3" fill="#1ea0cf"/><path d="M0.7 5 H9.3 M5 0.7 Q2.5 5 5 9.3 M5 0.7 Q7.5 5 5 9.3" fill="none" stroke="#f3f3f3" stroke-width="0.7"/></svg>
        www.vantorix.global
      </li>
    </ul>

    <svg class="back-footer" viewBox="0 0 481 38" preserveAspectRatio="none" aria-hidden="true">
      <rect x="0" y="27" width="230" height="11" fill="#1ea0cf"/>
      <path d="M234 0 H481 V38 H210 Q222 12 234 0Z" fill="#0b2236"/>
    </svg>
    <div class="footer-url">www.vantorix.com.au</div>
  </section>
</body>
</html>
```